Hair salon and Nail salon in Hawaii need a newspaper Ad design.

We need a newspaper Ad design for new open hair & nail salon in Waikiki Hawaii.Our Recommendation service for hair is "Head Spa" $30+tax and for nail is "Manicure Treatment Course" (Filing+Cuticle Care+Massage+Coloring) $20+tax.
We would like to see Hawaiian taste color and also having sense of luxury design. The ad size is W 5.0” x H 6.375”.
I would customers to know the shop place(Lanakila Crest Hotel 1F) , phone(808-555-0173), instagram(salonbrightwave) , our web site https://salonbrightwave.example and recommend services. For Web or Instagram , QR code is acceptable.

Target Market(s)

women & men

Industry/Entity Type

Beauty Salon

Font styles to use
Serif

Colors

Designer to choose colors to be used in the design.

Requirements
Must have
• Tagline for local customers. Shop Name is "SALON BRIGHTWAVE".the shop place(Lanakila Crest Hotel 1F) , phone(808-555-0173), instagram(salonbrightwave) and recommend services.
Nice to have
• Our services are competitive, but we don't want to be seen as just cheap and low quality.

```html
<!DOCTYPE html>
<html lang="en">
<head>
<meta charset="utf-8">
<title>Salon Brightwave – Newspaper Ad</title>
<link rel="stylesheet" href="https://fonts.googleapis.com/css2?family=Great+Vibes&family=Marcellus&family=Crimson+Pro:ital,wght@0,400;0,600;0,700;1,400&display=swap">
<style>
  :root {
    --red: #b3171c;
    --ink: #231f20;
    --paper: #ffffff;
    --paper-shade: #ececec;
    --rule: #9a9a9a;
    --mark: #2b1f1f;
    --skin-light: #f1ddd1;
    --skin-mid: #e4c2ae;
    --hair: #4a3128;
  }
  * { margin: 0; padding: 0; box-sizing: border-box; }
  html, body { width: 1200px; height: 877px; overflow: hidden; background: var(--paper); }
  .ad {
    position: relative;
    width: 1200px;
    height: 877px;
    background: linear-gradient(120deg, var(--paper-shade) 0%, var(--paper) 45%, var(--paper) 100%);
    font-family: "Marcellus", serif;
    color: var(--ink);
    overflow: hidden;
  }
  .ad > * { position: absolute; white-space: nowrap; }

  .model-photo {
    left: 600px; top: 0; width: 600px; height: 877px;
    background:
      radial-gradient(ellipse 45% 35% at 80% 20%, var(--hair) 0%, rgba(74,49,40,0) 100%),
      radial-gradient(ellipse 55% 60% at 72% 55%, var(--skin-mid) 0%, rgba(228,194,174,0) 100%),
      linear-gradient(90deg, rgba(241,221,209,0) 0%, var(--skin-light) 35%, var(--skin-light) 100%);
  }

  .headline-open {
    left: 62px; top: 30px;
    font-family: "Great Vibes", cursive;
    font-size: 150px; line-height: 1;
    color: var(--red);
  }
  .headline-type { left: 353px; top: 110px; font-size: 40px; line-height: 1; }
  .headline-in { left: 204px; top: 172px; font-size: 34px; line-height: 1; }
  .headline-place {
    left: 247px; top: 152px;
    font-family: "Crimson Pro", serif; font-weight: 700;
    font-size: 58px; line-height: 1; color: var(--red);
  }

  .service { font-family: "Crimson Pro", serif; line-height: 1; }
  .service-label { font-size: 15px; font-weight: 600; }
  .service-name { font-size: 32px; font-weight: 600; }
  .service-detail { font-size: 14px; font-weight: 600; display: block; margin-top: 4px; }
  .service-price { font-size: 32px; font-weight: 700; color: var(--red); display: block; margin-top: 8px; }
  .service-nail { left: 83px; top: 282px; }
  .service-nail .service-name { display: block; margin-top: 2px; }
  .service-hair { left: 401px; top: 311px; }

  .service-divider { left: 377px; top: 270px; width: 2px; height: 132px; background: var(--rule); }

  .contact-place {
    left: 83px; top: 468px;
    font-family: "Crimson Pro", serif; font-weight: 600;
    font-size: 38px; line-height: 1; color: var(--red);
  }
  .contact-phone {
    left: 80px; top: 506px;
    font-family: "Crimson Pro", serif; font-weight: 700;
    font-size: 74px; line-height: 1; color: var(--red); letter-spacing: 0.5px;
  }
  .contact-email {
    left: 83px; top: 576px;
    font-family: "Crimson Pro", serif; font-weight: 600;
    font-size: 38px; line-height: 1;
  }

  .brand-square { left: 83px; top: 697px; width: 112px; height: 108px; background: var(--mark); }
  .brand-name { left: 220px; top: 716px; font-size: 36px; line-height: 1; letter-spacing: 1px; }
  .brand-tagline {
    left: 222px; top: 758px;
    font-family: "Crimson Pro", serif; font-style: italic;
    font-size: 22px; line-height: 1;
  }
</style>
</head>
<body>
<main class="ad">
  <div class="model-photo" role="img" aria-label="Photo of a woman with an updo showing pink and yellow manicured nails and a spiked bracelet"></div>

  <span class="headline-open">Open</span>
  <span class="headline-type">Hair &amp; Nail Salon</span>
  <span class="headline-in">in</span>
  <span class="headline-place">Waikiki Hawaii</span>

  <div class="service service-nail">
    <span class="service-label">Nail is</span><span class="service-name" style="display:inline">"Manicure</span>
    <span class="service-name">Treatment Course"</span>
    <span class="service-detail">Filing + Cuticle Care + Massage + Coloring</span>
    <span class="service-price">$20 + tax</span>
  </div>
  <div class="service-divider"></div>
  <div class="service service-hair">
    <span class="service-label">Hair is</span><span class="service-name">"Head Spa"</span>
    <span class="service-price" style="margin-top:2px">$30 + tax</span>
  </div>

  <span class="contact-place">Lanakila Crest Hotel 1F</span>
  <span class="contact-phone">808-555-0173</span>
  <span class="contact-email">info@salonbrightwave.com</span>

  <div class="brand-square"></div>
  <span class="brand-name">SALON BRIGHTWAVE</span>
  <span class="brand-tagline">"Quality Care, Quality Hair"</span>
</main>
</body>
</html>
```